Reefline Systems

I run an aquarium service business covering all aspects of large scale saltwater aquariums. Design, installation, and service. My main customer base is corporations in Manhattan, but I also deal with smaller home or business aquariums in the tri-state area. I work with cutting edge equipment and service techniques and need to convey that.

Industry/Entity Type

Business

Contact Information for Business Card

REEFLINE SYSTEMS LLC
Daniel R. Hollworth
Owner
Main 203-555-0182
Cell 203-555-0147
Service.ReeflineSystems@examplemail.com

```html
<!DOCTYPE html>
<html lang="en">
<head>
<meta charset="utf-8">
<title>Reefline Systems – Business Card</title>
<link rel="stylesheet" href="https://fonts.googleapis.com/css2?family=Quicksand:wght@400;500;600&display=swap">
<style>
  :root {
    --page-bg: #4f5a5d;
    --card-mint: #c9ddd6;
    --card-mist: #e4eeeb;
    --card-white: #f6f9f9;
    --ink: #1f2426;
    --ink-soft: #2b3133;
    --accent-blue: #2f7fe0;
    --silver-dark: #4a4f52;
    --silver-light: #b8bec0;
  }
  * { margin: 0; padding: 0; box-sizing: border-box; }
  html, body {
    width: 1200px;
    height: 741px;
    overflow: hidden;
    background: var(--page-bg);
    font-family: "Quicksand", "Century Gothic", sans-serif;
  }
  .business-card {
    position: absolute;
    left: 150px;
    top: 108px;
    width: 900px;
    height: 524px;
    overflow: hidden;
    background:
      linear-gradient(180deg, rgba(255,255,255,0) 40%, rgba(255,255,255,0.55) 52%, rgba(255,255,255,0) 64%),
      linear-gradient(100deg, var(--card-mint) 0%, var(--card-mist) 45%, var(--card-white) 100%);
  }
  .company-name {
    position: absolute;
    left: 24px;
    top: 14px;
    font-size: 40px;
    font-weight: 500;
    letter-spacing: 2.2px;
    color: var(--ink);
    white-space: nowrap;
  }
  .seahorse-illustration {
    position: absolute;
    left: 219px;
    top: 86px;
    width: 155px;
    height: 326px;
    border-radius: 45% 45% 40% 40% / 20% 20% 30% 30%;
    background: radial-gradient(ellipse at 45% 40%, var(--silver-light) 0%, #7e8588 45%, var(--silver-dark) 100%);
    opacity: 0.85;
  }
  .contact-list {
    position: absolute;
    left: 386px;
    top: 218px;
    right: 14px;
    list-style: none;
  }
  .contact-item {
    display: flex;
    align-items: center;
    height: 39px;
    font-size: 21px;
    font-weight: 500;
    color: var(--ink-soft);
    letter-spacing: 0.1px;
    white-space: nowrap;
  }
  .contact-icon {
    width: 22px;
    height: 22px;
    margin-right: 26px;
    flex: none;
    fill: var(--accent-blue);
  }
  .person-role {
    position: absolute;
    right: 29px;
    top: 412px;
    font-size: 34px;
    font-weight: 500;
    letter-spacing: 1px;
    color: var(--accent-blue);
  }
  .person-name {
    position: absolute;
    right: 24px;
    top: 452px;
    font-size: 46px;
    font-weight: 500;
    letter-spacing: 1.5px;
    color: var(--ink);
    white-space: nowrap;
  }
</style>
</head>
<body>
  <section class="business-card">
    <h1 class="company-name">Reefline Systems LLC</h1>

    <div class="seahorse-illustration" role="img" aria-label="Metallic mechanical seahorse sculpture with rising bubbles"></div>

    <ul class="contact-list">
      <li class="contact-item">
        <svg class="contact-icon" viewBox="0 0 24 24" aria-hidden="true"><path d="M6.6 10.8c1.4 2.8 3.8 5.1 6.6 6.6l2.2-2.2c.3-.3.7-.4 1-.2 1.1.4 2.3.6 3.6.6.6 0 1 .4 1 1V20c0 .6-.4 1-1 1C10.6 21 3 13.4 3 4c0-.6.4-1 1-1h3.5c.6 0 1 .4 1 1 0 1.3.2 2.5.6 3.6.1.3 0 .7-.2 1L6.6 10.8z"/></svg>
        <span class="contact-text">203-555-0182</span>
      </li>
      <li class="contact-item">
        <svg class="contact-icon" viewBox="0 0 24 24" aria-hidden="true"><path d="M8 2h8c1.1 0 2 .9 2 2v16c0 1.1-.9 2-2 2H8c-1.1 0-2-.9-2-2V4c0-1.1.9-2 2-2zm0 3v13h8V5H8zm4 14.2a1 1 0 1 0 0 2 1 1 0 0 0 0-2z"/></svg>
        <span class="contact-text">203-555-0147</span>
      </li>
      <li class="contact-item">
        <svg class="contact-icon" viewBox="0 0 24 24" aria-hidden="true"><path d="M3 6h18v12H3V6zm2 2v.3l7 4.4 7-4.4V8l-7 4.3L5 8z"/></svg>
        <span class="contact-text">Service.ReeflineSystems@examplemail.com</span>
      </li>
    </ul>

    <p class="person-role">Owner</p>
    <p class="person-name">Daniel R. Hollworth</p>
  </section>
</body>
</html>
```